We are a Leadership Specialist Boutique Business that is launching a residential womans workshop....

We need a post card which will include our logo, an overview of our workshop, a catch statement on one side and on the other side dates, venue, facilitators and contacts to book the workshop. The postcards will be distributed at an Global Sisterhood Harvest Lunch. They will be placed at each setting of the lunch attendees. The company QBR running the lunch is a sponsor of our business.

Target Market(s)

Women supervisor to middle management positions or own business

Industry/Entity Type

Academic Training

Font styles to use
Serif

Colors
34a7d8

Requirements
Must have
• Use Colour Palette on docs attached, Logo, Workshop overview either the Circle Theory or the Core Philosophy Text,
• The dates, venue, all costs of the program including discount code. One catch sentence that grabs the audience from the content I have provided that appeals to the designer
• Must have these contacts.
• Website: brightpathforwardgroup.com,au
• Email: Info@brightpathforwardgroup.com.au.
• Phone: 0419372605
Nice to have
• Facilitators Photos and names

```html
<!DOCTYPE html>
<html lang="en">
<head>
<meta charset="utf-8">
<title>Leadership Workshop Postcard</title>
<link rel="stylesheet" href="https://fonts.googleapis.com/css2?family=Montserrat:wght@700;800&family=Nunito:wght@400;600&display=swap">
<style>
  :root {
    --blue: #29a6d9;
    --mint: #b9e0d4;
    --ink: #222222;
    --white: #ffffff;
    --backdrop: #808080;
    --photo-dark: #3e4144;
    --photo-light: #a9acae;
  }
  * { margin: 0; padding: 0; box-sizing: border-box; }
  html, body { width: 1200px; height: 1200px; overflow: hidden; }
  body { background: var(--backdrop); position: relative; font-family: "Nunito", sans-serif; color: var(--ink); }
  .card { position: absolute; background: var(--white); overflow: hidden; }
  .card-front { left: 220px; top: 42px; width: 760px; height: 506px; }
  .card-back { left: 216px; top: 624px; width: 770px; height: 512px; }
  .card-shapes { position: absolute; inset: 0; }
  .abs { position: absolute; white-space: nowrap; }

  .front-title { left: 22px; top: 26px; font-family: "Montserrat", sans-serif; font-weight: 800; font-size: 25px; line-height: 30px; color: var(--white); letter-spacing: 0.3px; }
  .tab-label { left: 22px; font-family: "Nunito", sans-serif; font-weight: 600; font-size: 22px; line-height: 30px; color: var(--white); }
  .tab-text { left: 22px; font-size: 17.5px; line-height: 21.5px; }
  .phone-icon { left: 22px; top: 456px; width: 32px; height: 32px; }
  .phone-number { left: 80px; top: 440px; font-family: "Montserrat", sans-serif; font-weight: 800; font-size: 46px; line-height: 60px; color: var(--white); letter-spacing: 0.5px; }

  .brand-name { left: 610px; top: 70px; width: 130px; text-align: center; font-family: "Nunito", sans-serif; font-weight: 600; font-size: 46px; line-height: 56px; color: var(--white); }

  .back-title { left: 32px; top: 23px; font-family: "Nunito", sans-serif; font-weight: 600; font-size: 24px; line-height: 34px; color: var(--white); }
  .back-subtitle { left: 54px; top: 68px; font-size: 22px; line-height: 28px; color: var(--blue); font-weight: 600; }
  .outline-list { list-style: none; }
  .outline-item { position: absolute; left: 56px; font-size: 16px; line-height: 19.6px; white-space: nowrap; }
  .tick { position: absolute; left: -22px; top: 3px; width: 14px; height: 14px; }
  .contact { left: 56px; font-size: 16px; line-height: 20px; color: var(--white); }
  .contact-icon { position: absolute; left: -24px; top: 3px; width: 14px; height: 14px; }

  .stamp-box { left: 634px; top: 117px; width: 94px; height: 85px; border: 1px solid #888; }
  .address-line { left: 512px; width: 216px; height: 1px; background: #999; }
</style>
</head>
<body>

<section class="card card-front">
  <svg class="card-shapes" viewBox="0 0 760 506" width="760" height="506">
    <defs>
      <linearGradient id="photoTone" x1="0" y1="0" x2="1" y2="1">
        <stop offset="0" stop-color="var(--photo-dark)"/>
        <stop offset="0.5" stop-color="var(--photo-light)"/>
        <stop offset="1" stop-color="#6b6f78"/>
      </linearGradient>
    </defs>
    <polygon points="0,13 472,13 444,90 0,90" fill="var(--blue)"/>
    <polygon points="0,106 146,106 158,144 0,144" fill="var(--blue)"/>
    <polygon points="0,176 104,176 116,212 0,212" fill="var(--blue)"/>
    <polygon points="0,261 166,261 178,298 0,298" fill="var(--blue)"/>
    <polygon points="0,426 404,426 472,506 0,506" fill="var(--blue)"/>
    <g role="img" aria-label="Photo of three young women in front of a chalkboard covered in maths formulas">
      <polygon points="472,0 760,0 760,506 472,506 332,374" fill="url(#photoTone)"/>
    </g>
    <polyline points="388,198 326,374 378,421" fill="none" stroke="var(--blue)" stroke-width="7"/>
  </svg>

  <h1 class="abs front-title">THE CORE PHILOSOPHY OF THE<br>PROGRAM</h1>

  <h2 class="abs tab-label" style="top:110px">Worldview</h2>
  <p class="abs tab-text" style="top:148px">A view Held inside of us as to how things work</p>

  <h2 class="abs tab-label" style="top:179px">Biases</h2>
  <p class="abs tab-text" style="top:215px">Our own behaviours and the behaviours of<br>others that reinforce this worldviews</p>

  <h2 class="abs tab-label" style="top:265px">Error Scripts</h2>
  <p class="abs tab-text" style="top:305px">Stories implanted by us or other that<br>limits our potential</p>
  <p class="abs tab-text" style="top:353px">Rewiting a new Personal Narrative<br>allows us to shatter our own glass<br>celing</p>

  <svg class="abs phone-icon" viewBox="0 0 32 32">
    <circle cx="16" cy="16" r="15" fill="var(--white)"/>
    <path d="M11 8 l3 0 l1.5 4.5 l-2 1.5 q1.5 3.5 5 5 l1.5 -2 l4.5 1.5 l0 3 q-1 2 -3 2 q-7 -0.5 -12 -6.5 q-2.5 -3.5 -2.5 -6 q0 -2 2 -3z" fill="var(--ink)"/>
  </svg>
  <p class="abs phone-number">0419372605</p>

  <p class="abs brand-name">rise</p>
</section>

<section class="card card-back">
  <svg class="card-shapes" viewBox="0 0 770 512" width="770" height="512">
    <polygon points="0,0 374,0 500,452 510,512 0,512" fill="var(--mint)"/>
    <polygon points="0,16 292,16 304,62 0,62" fill="var(--blue)"/>
    <polygon points="0,452 500,452 510,512 0,512" fill="var(--blue)"/>
    <line x1="394" y1="50" x2="464" y2="320" stroke="var(--blue)" stroke-width="5"/>
  </svg>

  <h1 class="abs back-title">PROGRAM OUTLINE</h1>
  <h2 class="abs back-subtitle">program and upcoming Dates</h2>

  <ul class="outline-list">
    <li class="outline-item" style="top:102px"><svg class="tick" viewBox="0 0 14 14"><circle cx="7" cy="7" r="7" fill="var(--blue)"/><path d="M3.8 7.2 l2.2 2.2 l4.2 -4.4" fill="none" stroke="var(--white)" stroke-width="1.8"/></svg>2 days residential-26th to 28th may 2019</li>
    <li class="outline-item" style="top:132px"><svg class="tick" viewBox="0 0 14 14"><circle cx="7" cy="7" r="7" fill="var(--blue)"/><path d="M3.8 7.2 l2.2 2.2 l4.2 -4.4" fill="none" stroke="var(--white)" stroke-width="1.8"/></svg>May Venue-The Linden Ridge Valley, Ashgrove<br>NSW</li>
    <li class="outline-item" style="top:176px"><svg class="tick" viewBox="0 0 14 14"><circle cx="7" cy="7" r="7" fill="var(--blue)"/><path d="M3.8 7.2 l2.2 2.2 l4.2 -4.4" fill="none" stroke="var(--white)" stroke-width="1.8"/></svg>Future Programs-August,October,March Why</li>
    <li class="outline-item" style="top:205px"><svg class="tick" viewBox="0 0 14 14"><circle cx="7" cy="7" r="7" fill="var(--blue)"/><path d="M3.8 7.2 l2.2 2.2 l4.2 -4.4" fill="none" stroke="var(--white)" stroke-width="1.8"/></svg>The program is emersive and wholistic which<br>includes development of your life and leadership<br>skills, by rewriting your narrative and a personal<br>action plan for change support &amp; Program Inclusions</li>
    <li class="outline-item" style="top:291px"><svg class="tick" viewBox="0 0 14 14"><circle cx="7" cy="7" r="7" fill="var(--blue)"/><path d="M3.8 7.2 l2.2 2.2 l4.2 -4.4" fill="none" stroke="var(--white)" stroke-width="1.8"/></svg>PSI Assessment, leadership skills sessions,<br>indevidual coaching sessions, guest speakers,<br>body wellness therapists as well as<br>accomodation and all meals are included<br>investment for May 2019 Program</li>
    <li class="outline-item" style="top:390px"><svg class="tick" viewBox="0 0 14 14"><circle cx="7" cy="7" r="7" fill="var(--blue)"/><path d="M3.8 7.2 l2.2 2.2 l4.2 -4.4" fill="none" stroke="var(--white)" stroke-width="1.8"/></svg>$3,495 (Early Bird Book by 26th April) $3,095</li>
    <li class="outline-item" style="top:420px"><svg class="tick" viewBox="0 0 14 14"><circle cx="7" cy="7" r="7" fill="var(--blue)"/><path d="M3.8 7.2 l2.2 2.2 l4.2 -4.4" fill="none" stroke="var(--white)" stroke-width="1.8"/></svg>Quote QBR Cord 9455 for a further $100 Discount</li>
  </ul>

  <p class="abs contact" style="top:460px"><svg class="contact-icon" viewBox="0 0 14 14"><circle cx="7" cy="7" r="6.3" fill="var(--white)" stroke="var(--ink)" stroke-width="1"/><ellipse cx="7" cy="7" rx="2.8" ry="6.3" fill="none" stroke="var(--ink)" stroke-width="0.9"/><line x1="0.7" y1="7" x2="13.3" y2="7" stroke="var(--ink)" stroke-width="0.9"/><line x1="1.8" y1="4" x2="12.2" y2="4" stroke="var(--ink)" stroke-width="0.8"/><line x1="1.8" y1="10" x2="12.2" y2="10" stroke="var(--ink)" stroke-width="0.8"/></svg>brightpathforwardgroup.com,au</p>
  <p class="abs contact" style="top:488px"><svg class="contact-icon" viewBox="0 0 14 14"><circle cx="7" cy="7" r="7" fill="var(--white)"/><rect x="3" y="4.5" width="8" height="5.5" fill="var(--ink)"/><path d="M3 4.5 l4 3 l4 -3" fill="none" stroke="var(--white)" stroke-width="0.9"/></svg>Info@brightpathforwardgroup.com.au.</p>

  <div class="abs stamp-box"></div>
  <div class="abs address-line" style="top:251px"></div>
  <div class="abs address-line" style="top:301px"></div>
  <div class="abs address-line" style="top:350px"></div>
  <div class="abs address-line" style="top:398px"></div>
</section>

</body>
</html>
```